Plimsoo car advertisement

de website moet uit minimaal 3 pagina's bestaan. 1 pagina als een landingspagina. 1 pagina voor consumenten die hun auto willen laten beplakken met bedrijfsreclame en 1 pagina voor bedrijven / consumenten die hun bedrijfsreclame op een consumentenauto wilt plaatsen.

de website moet echt een happy website zijn. consumenten kunnen geld verdienen met reclame op hun auto te laten zetten en bedrijven kunnen voor een relatief goedkoop bedrag hun bedrijfsreclame op een auto laten zetten. die auto rijdt dan rond en veel mensen zien de reclame.

beide pagina's moeten dus een glimlach opleveren.

het doel van de startpagina is dat je door kunt gaan naar de consumenten en de bedrijfspagina.

gebruik leuke, vrolijke kleuren en vormen en zorg dat de mensen een glimlach krijgen als ze naar de website kijken.

doelgroep is consumenten die een auto rijden en geld willen verdienen met hun auto en de zakelijke ondernemer die voor een goedkoop bedrag zijn bedrijfsreclame met een full carwrap kan laten zien aan de buitenwereld.

doordat consumenten zich bij ons aanmelden hebben wij een database met auto's en weten we hoeveel deze auto's rijden en in welke regio's ze rijden en wat voor auto ze rijden. allemaal hele belangrijke informatie voor een ondernemer die reclame wilt maken op ene specifieke auto type en in een bepaalde regio.

-

website should consist of at least 3 pages. 1 landing page, 1 customer page and 1 business page. landing page let's the visitor choose wether he / she is a customer with a car and wants to allow his car to be fully carwrapped or he / she is a business owner who wants to place his advertisement on a car.

website should be a really happy joyfull website and bring a smile to the visitor. beause the customer can earn money (200 euro / month nett) by allowing advertisements on his car (full car wrap) and the business owner because for a low price he can advertise.

when customers that owns a car register themselves with our website we build a database with cars in specific locations. a business owner wants to advertise his product into a specific region. this is very valuable information.

agreement is 1 year for a customer to have advertisements on his car and for a business to advertise. after that year, the advertisements are safely removed from the car and new advertisement agreements can be made. a business can place advertisements (full carwrap) already for 795 euro's., Details for my new Web Design Project will be added soon. , de website moet uit minimaal 3 pagina's bestaan. 1 pagina als een landingspagina. 1 pagina voor consumenten die hun auto willen laten beplakken met bedrijfsreclame en 1 pagina voor bedrijven / consumenten die hun bedrijfsreclame op een consumentenauto wilt plaatsen.

Target Market(s)

customers who has a car
businesses who want to advertise their business / product on a car

Industry/Entity Type

Business

Requirements
Must have
• website should be playfull, colorfull and a joy to look at and work with. altough functoinality is very limited visitors need to be intrigued to proceed to contact plimsoo.
Nice to have
• nice graphics, moving images, a "living" website (not so static)

```html
<!DOCTYPE html>
<html lang="en">
<head>
<meta charset="utf-8">
<title>Plimsoo Car</title>
<link rel="stylesheet" href="https://fonts.googleapis.com/css2?family=Arimo:wght@400;700&family=Open+Sans:wght@400;600;700&display=swap">
<style>
  :root {
    --brand-blue: #0261b3;
    --deep-blue: #0457a3;
    --link-blue: #1a63b0;
    --white: #ffffff;
    --panel-grey: #efefef;
    --field-grey: #f2f2f4;
    --text-grey: #555555;
    --orange: #f7941d;
    --orange-dark: #f07a0a;
    --nav-active: #f8a21c;
    --help-green: #3aa43a;
  }
  * { box-sizing: border-box; margin: 0; padding: 0; }
  html, body { width: 1200px; height: 1107px; overflow: hidden; }
  body {
    position: relative;
    background: var(--brand-blue);
    font-family: "Open Sans", Arial, sans-serif;
    color: var(--text-grey);
  }
  .abs { position: absolute; }

  .page-panel { left: 57px; top: 125px; width: 1086px; height: 875px; background: var(--white); border-radius: 8px; }
  .logo-tab { left: 57px; top: 14px; width: 221px; height: 115px; background: var(--white); border-radius: 22px 22px 0 0; }
  .logo-tab::after { content: ""; position: absolute; right: -34px; bottom: -4px; width: 34px; height: 30px;
    background: radial-gradient(circle at 100% 0, transparent 29px, var(--white) 30px); }
  .brand-mark { left: 150px; top: 28px; width: 58px; height: 58px; border-radius: 50%; background: var(--link-blue); }
  .brand-name { left: 72px; top: 87px; font-family: "Open Sans", sans-serif; font-weight: 700; font-size: 27px;
    color: var(--link-blue); letter-spacing: 0.2px; white-space: nowrap; }

  .search-field { left: 620px; top: 32px; width: 185px; height: 34px; background: var(--field-grey); border-radius: 4px; border: 1px solid #d8d8de; }
  .search-button { left: 815px; top: 32px; width: 81px; height: 34px; border-radius: 4px;
    background: linear-gradient(#ffa43a, var(--orange-dark)); color: var(--white);
    font-family: "Arimo", sans-serif; font-weight: 700; font-size: 16px; text-align: center; line-height: 34px; }
  .utility-links { left: 923px; top: 43px; font-family: "Arimo", sans-serif; font-weight: 700; font-size: 14px; color: var(--white); }
  .utility-links span { margin: 0 6px; }

  .main-nav { top: 96px; font-family: "Arimo", sans-serif; font-weight: 700; font-size: 14px; color: var(--white); }
  .main-nav.active { color: var(--nav-active); }
  .social { top: 88px; width: 27px; height: 27px; }

  .lead-form { left: 72px; top: 140px; width: 295px; height: 331px;
    background: linear-gradient(90deg, var(--deep-blue), #1c7fc9 50%, var(--deep-blue)); }
  .field { left: 86px; width: 262px; height: 32px; background: var(--field-grey);
    font-size: 13px; color: #8a8a8a; padding: 6px 11px; }
  .submit { left: 91px; top: 416px; width: 262px; height: 37px; border-radius: 4px;
    background: linear-gradient(#fcb24a, var(--orange-dark)); color: #a6561a;
    font-weight: 700; font-size: 15px; text-align: center; line-height: 37px; }

  .side-box { left: 72px; width: 295px; background: var(--panel-grey); }
  .box-head { height: 41px; background: linear-gradient(#ffffff, #d9d9d9);
    font-weight: 600; font-size: 16px; color: #222; padding: 9px 12px; }
  .feature-item { left: 86px; width: 266px; height: 34px; border-bottom: 1px solid #d9d9d9;
    font-size: 15px; color: var(--link-blue); padding-left: 25px; line-height: 26px; white-space: nowrap; }
  .feature-item::before { content: ""; position: absolute; left: 0; top: 9px; width: 10px; height: 10px; background: #6d88b4; }
  .feature-item::after { content: ""; position: absolute; left: 3px; top: 11px; border-left: 5px solid #fff; border-top: 3px solid transparent; border-bottom: 3px solid transparent; }

  .photo { background: linear-gradient(160deg, #3f5a32, #8f9a8a 45%, #c8d0da 60%, #4c4a48); }
  .photo-workshop { background: linear-gradient(160deg, #d8d2c4, #e4e4e4 50%, #6e7f9e); }

  .content-box { background: var(--panel-grey); }
  .welcome-head { font-weight: 600; font-size: 20px; color: var(--link-blue); padding: 7px 20px; }
  .body-copy { font-size: 12px; line-height: 19.5px; color: var(--text-grey); }
  .event-copy { font-size: 12px; line-height: 19.6px; color: #333; }

  .help-tab { left: 1165px; top: 194px; width: 40px; height: 112px; background: var(--help-green);
    border-radius: 8px 0 0 8px; border: 2px solid #2a7a2a; }
  .help-tab span { position: absolute; left: 8px; top: 92px; transform: rotate(-90deg); transform-origin: 0 0;
    color: var(--white); font-weight: 700; font-size: 18px; white-space: nowrap; }
  .help-dot { left: 1162px; top: 186px; width: 24px; height: 24px; border-radius: 50%; background: #7ed321; border: 2px solid #4aa81a; }

  .footer-links { left: 0; width: 1200px; top: 1023px; text-align: center; font-family: "Arimo", sans-serif;
    font-weight: 700; font-size: 14px; color: var(--white); word-spacing: 1px; }
  .footer-links span { margin: 0 12px; }
  .copyright { left: 0; width: 1200px; top: 1057px; text-align: center; font-size: 12px; color: var(--white); }
</style>
</head>
<body>
  <div class="abs page-panel"></div>
  <div class="abs logo-tab"></div>
  <div class="abs brand-mark"></div>
  <div class="abs brand-name">PLIMSOO CAR</div>

  <div class="abs search-field"></div>
  <div class="abs search-button">Search</div>
  <div class="abs utility-links">Customer Login<span>|</span>Contact Us</div>

  <nav>
    <div class="abs main-nav active" style="left:383px">HOME</div>
    <div class="abs main-nav" style="left:471px">ABOUT&nbsp; US</div>
    <div class="abs main-nav" style="left:590px">OUR SERVICES</div>
    <div class="abs main-nav" style="left:732px">OUR NEWS</div>
    <div class="abs main-nav" style="left:852px">CONTACT US</div>
  </nav>

  <svg class="abs social" style="left:1022px" viewBox="0 0 27 27" aria-label="Email">
    <circle cx="13.5" cy="13.5" r="13" fill="#fff"/><circle cx="13.5" cy="13.5" r="11" fill="#1a63b0"/>
    <rect x="7" y="9" width="13" height="9" rx="1" fill="none" stroke="#fff" stroke-width="1.6"/>
    <path d="M7.5 9.5 13.5 14 19.5 9.5" fill="none" stroke="#fff" stroke-width="1.6"/>
  </svg>
  <svg class="abs social" style="left:1052px" viewBox="0 0 27 27" aria-label="Phone">
    <circle cx="13.5" cy="13.5" r="13" fill="#fff"/><circle cx="13.5" cy="13.5" r="11" fill="#1a63b0"/>
    <path d="M9 7.5c-1 .8-1.5 2 .2 4.8 1.6 2.8 3.6 4.6 6 5.7 1.2.5 2.4.2 3-.9l-2.3-2.1-1.6 1c-1.6-.9-2.8-2.2-3.6-3.8l1.2-1.4L10.6 7z" fill="#fff"/>
  </svg>
  <svg class="abs social" style="left:1083px" viewBox="0 0 27 27" aria-label="Share">
    <circle cx="13.5" cy="13.5" r="13" fill="#fff"/><circle cx="13.5" cy="13.5" r="11" fill="#1a63b0"/>
    <path d="M10 13.5 17 9.5M10 13.5 17 17.5" stroke="#fff" stroke-width="1.6"/>
    <circle cx="9.5" cy="13.5" r="2.2" fill="#fff"/><circle cx="17.5" cy="9" r="2.2" fill="#fff"/><circle cx="17.5" cy="18" r="2.2" fill="#fff"/>
  </svg>
  <svg class="abs social" style="left:1113px" viewBox="0 0 27 27" aria-label="Location">
    <circle cx="13.5" cy="13.5" r="13" fill="#fff"/><circle cx="13.5" cy="13.5" r="11" fill="#1a63b0"/>
    <path d="M13.5 20.5s-5-5.2-5-8.7a5 5 0 0 1 10 0c0 3.5-5 8.7-5 8.7z" fill="#fff"/>
    <circle cx="13.5" cy="11.8" r="1.9" fill="#1a63b0"/>
  </svg>

  <form class="abs lead-form"></form>
  <div class="abs field" style="top:159px">Name</div>
  <div class="abs field" style="top:200px">Email</div>
  <div class="abs field" style="top:242px">Phone</div>
  <div class="abs field" style="top:284px">Cell</div>
  <div class="abs field" style="top:323px;height:75px">Decription</div>
  <div class="abs submit">SUBMIT YOUR DETAILS</div>

  <section class="abs side-box" style="top:484px;height:268px">
    <div class="box-head" style="margin:3px 44px 0 7px;width:278px">Slide Show</div>
  </section>
  <div class="abs photo-workshop" style="left:81px;top:533px;width:275px;height:210px" role="img" aria-label="Technician applying an advertising wrap to a car door"></div>

  <section class="abs side-box" style="top:772px;height:204px">
    <div class="box-head" style="margin:6px 10px 0 7px;width:278px">Featured</div>
  </section>
  <div class="abs feature-item" style="top:826px">I drive a car, pay me!</div>
  <div class="abs feature-item" style="top:860px">I want to advertise</div>
  <div class="abs feature-item" style="top:893px">How a full wrap works</div>
  <div class="abs feature-item" style="top:926px;border-bottom:none">Regions and car types</div>

  <div class="abs photo" style="left:381px;top:140px;width:749px;height:558px" role="img" aria-label="Small hatchback with a full colourful advertising wrap parked under trees"></div>

  <section class="abs content-box" style="left:381px;top:708px;width:518px;height:268px">
    <div class="box-head welcome-head" style="margin:6px 6px 0 6px;height:42px">Welcome to our website</div>
    <p class="abs body-copy" style="left:19px;top:55px;width:490px">Plimsoo brings car owners and businesses together. Let your car wear a colourful full wrap and earn 200 euro net every month. Businesses reach thousands of people each day as the car drives through the region they choose, on the car type they want. After one year the wrap is removed safely.</p>
    <p class="abs body-copy" style="left:19px;top:153px;width:490px">Business owner? Put your advertising on a car with a full wrap from just 795 euro for a whole year of smiles on the road.</p>
    <p class="abs body-copy" style="left:19px;top:230px;width:490px">Sign up today and bring a smile to every road you drive.</p>
  </section>

  <section class="abs content-box" style="left:911px;top:708px;width:216px;height:129px">
    <div class="box-head" style="margin:2px 3px 0 3px;height:33px;padding:4px 6px;font-size:15.5px">Community Event</div>
    <p class="abs event-copy" style="left:9px;top:39px;width:182px">Wrap day: watch our team put a full colour wrap on a car, with coffee, music and fun.</p>
  </section>
  <section class="abs content-box" style="left:911px;top:849px;width:216px;height:127px">
    <div class="box-head" style="margin:2px 3px 0 3px;height:33px;padding:4px 8px;font-size:15.5px">Community Event</div>
    <p class="abs event-copy" style="left:9px;top:41px;width:182px">Happy drive: wrapped cars ride together through town. Join in and wave to everyone.</p>
  </section>

  <div class="abs help-tab"><span>live help</span></div>
  <div class="abs help-dot"></div>

  <footer>
    <div class="abs footer-links">HOME<span>|</span>TERMS OF USE &amp; DISCLAIMER<span>|</span>PRIVACY<span>|</span>SITEMAP</div>
    <div class="abs copyright">Copyrighte text here</div>
  </footer>
</body>
</html>
```